Online Travel Agency card design with 2 logos

Need a two sided business card design for online tourism agency which is based in Istanbul Turkey.
Need a business card design where it shows the travel agency logo but also the logo and information of the parent company as well.Parent company logo is just text with 2 different colors. (Arial font with text TemaVista "Tema"- hex #172841 and "Vista" hex-#FF7F00)
Both logos are uploaded.
Target Market(s)
travel , online
Industry/Entity Type
Travel
Contact Information for Business Card
The information on the card should be as :
Travel Agency Logo logo (rnlogo)
Parent Company logo(temalogo)
Company information :TemaVista Turizm ve Bilgi Teknolojileri A.Ş
Address of company
Tel
Email
Name
Position(english and turkish)
Look and feel
Each slider illustrates characteristics of the customer's brand and the style your logo design should communicate.

```html
<!DOCTYPE html>
<html lang="en">
<head>
<meta charset="utf-8">
<title>serinrota business card</title>
<link href="https://fonts.googleapis.com/css2?family=Arimo:ital,wght@0,400;0,700;1,400;1,700&display=swap" rel="stylesheet">
<style>
  :root {
    --navy: #172841;
    --sky: #6ccbe6;
    --mist: #dcdfe3;
    --paper: #f7f7f7;
    --orange: #ff7f00;
    --ink-light: #ffffff;
    --stage: #1d1d1f;
  }
  * { box-sizing: border-box; margin: 0; padding: 0; }
  html, body { width: 1200px; height: 974px; overflow: hidden; }
  body {
    background: var(--stage);
    font-family: "Arimo", Arial, sans-serif;
    position: relative;
  }
  .card {
    position: absolute;
    width: 560px;
    height: 320px;
    border-radius: 16px;
    overflow: hidden;
  }
  .card-front { left: 80px; top: 500px; background: var(--paper); }
  .card-back { left: 560px; top: 130px; background: var(--navy); }
  .card svg.bg { position: absolute; inset: 0; }

  .person { position: absolute; left: 40px; top: 40px; color: var(--navy); }
  .person-name { font-weight: 700; font-size: 20px; letter-spacing: 0.3px; }
  .person-role { font-style: italic; font-size: 13px; margin-top: 3px; }

  .brand {
    position: absolute;
    display: flex; align-items: center; gap: 8px;
  }
  .brand-mark { width: 30px; height: 30px; border-radius: 50%; }
  .brand-name { font-weight: 700; font-size: 34px; letter-spacing: -0.5px; }
  .card-front .brand { left: 270px; top: 108px; }
  .card-front .brand-mark { background: var(--navy); }
  .card-front .brand-name { color: var(--navy); }
  .card-back .brand { left: 250px; top: 120px; }
  .card-back .brand-mark { background: none; border: 2px solid var(--sky); }
  .card-back .brand-name { color: var(--ink-light); }

  .contacts {
    position: absolute; left: 30px; top: 182px;
    list-style: none; color: var(--ink-light); font-size: 14px;
  }
  .contacts li { display: flex; align-items: center; gap: 10px; height: 22px; }
  .contacts svg { width: 14px; height: 14px; }

  .address {
    position: absolute; right: 40px; bottom: 16px;
    color: var(--ink-light); font-size: 14px; line-height: 1.4; text-align: left;
  }
  .parent-name {
    position: absolute; right: 50px; bottom: 48px;
    color: var(--orange); font-weight: 700; font-size: 24px;
  }
</style>
</head>
<body>

<section class="card card-front">
  <svg class="bg" width="560" height="320" viewBox="0 0 560 320">
    <path d="M0,106 C150,116 260,156 340,216 C400,258 480,206 560,186 L560,198 C480,218 400,270 340,228 C260,168 150,128 0,118 Z" fill="var(--mist)"/>
    <path d="M0,118 C150,128 260,168 340,228 C400,270 480,218 560,198 L560,210 C480,230 400,282 340,240 C260,180 150,140 0,130 Z" fill="var(--sky)"/>
    <path d="M0,130 C150,140 260,180 340,240 C400,282 480,230 560,210 L560,320 L0,320 Z" fill="var(--navy)"/>
  </svg>
  <div class="person">
    <p class="person-name">DENIZ ARMAN</p>
    <p class="person-role">President</p>
  </div>
  <div class="brand">
    <span class="brand-mark"></span>
    <span class="brand-name">serinrota</span>
  </div>
  <ul class="contacts">
    <li><svg viewBox="0 0 14 14"><path d="M3 1 L5 1 L6 4 L4.5 5 C5.5 7 7 8.5 9 9.5 L10 8 L13 9 L13 11 C13 12 12 13 11 13 C6 12.5 1.5 8 1 3 C1 2 2 1 3 1 Z" fill="var(--sky)"/></svg>(612) 480 317</li>
    <li><svg viewBox="0 0 14 14"><rect x="3.5" y="1" width="7" height="12" rx="1.5" fill="none" stroke="var(--sky)" stroke-width="1.5"/></svg>(612) 480 318</li>
    <li><svg viewBox="0 0 14 14"><rect x="1" y="3" width="12" height="8" fill="var(--sky)"/><path d="M1 3 L7 8 L13 3" fill="none" stroke="var(--navy)" stroke-width="1"/></svg>info@serinrota.com</li>
    <li><svg viewBox="0 0 14 14"><circle cx="7" cy="7" r="5.5" fill="none" stroke="var(--sky)" stroke-width="1.3"/><path d="M1.5 7 H12.5 M7 1.5 V12.5" stroke="var(--sky)" stroke-width="1"/></svg>www.serinrota.com</li>
  </ul>
  <p class="address">845 Harbor Lane Suite 210<br>Lakeview, IL 60321</p>
</section>

<section class="card card-back">
  <svg class="bg" width="560" height="320" viewBox="0 0 560 320">
    <path d="M0,0 L220,0 C200,120 140,230 0,250 Z" fill="var(--sky)"/>
    <path d="M0,250 C140,230 200,120 220,0 L232,0 C214,132 150,248 0,266 Z" fill="var(--paper)" opacity="0.9"/>
  </svg>
  <div class="brand">
    <span class="brand-mark"></span>
    <span class="brand-name">serinrota</span>
  </div>
  <p class="parent-name">TemaVista</p>
</section>

</body>
</html>
```